Advertising flyer for proofreading business.

Hello everyone,

I need an advertising flyer for a new proofreading company in Australia.

I would like your design in be in two sizes:
- A4 (to be posted on noticeboards),
- A6 (to be printed in larger quantity to give away)
(please see the size specification file attached).

The text file is attached (Ad Text) and it contains lots of information. Please feel free to include your choice of text from the text file, but please include Poster title, and highlight 'ESL' and students discounts.

I understand that it is impossible to include the same amount of information on A6 and A4, so please feel free to chose what fits on each of them, but please keep the design similar.

I have attached our company logo, but feel free to adjust it to the poster design (feel free to change the color as well). The original logo file contains circle around it, please feel free to remove it and include only the typeset as it can be seen here: http://www.lexmarka.com.au/.

Flyers will be printed, so please see the specification file for details.

I will do my best to respond to feedback as soon as possible.

I appreciate your participation, time and help,
Best wishes,
Bartosz

Target Market(s)

Students, authors

Industry/Entity Type

Business

Colors

Designer to choose colors to be used in the design.

Requirements
Must have
• It would be good if poster is easy to spot on busy noticeboards and attract attention.
• Please keep the poster in the positive/optimistic mood, and so that it focuses on students, maybe photos of graduates(?).
• Poster title,
• Please include the list of proof-read documents as they are described in the attached text file (Ad Text).
• Please highlight students discounts and ESL.
Nice to have
• I would like to leave the creative freedom to all designers so at this point I have not adjusted the Look and Feel sliders. Please feel free to offer your own take on this.
• It would be nice if most of the text could be fit to the poster.

```html
<!DOCTYPE html>
<html lang="en">
<head>
<meta charset="utf-8">
<title>Lexmarka – Professional English Language Proofreading</title>
<link href="https://fonts.googleapis.com/css2?family=Libre+Baskerville:ital,wght@0,400;1,400;1,700&family=Open+Sans:ital,wght@0,400;0,600;1,400;1,600&display=swap" rel="stylesheet">
<style>
  :root{
    --magenta:#a3195b;
    --magenta-dark:#7d1044;
    --magenta-soft:#c9407e;
    --blush:#f6e3ec;
    --ink:#3d2a33;
    --white:#ffffff;
  }
  *{margin:0;padding:0;box-sizing:border-box}
  html,body{width:853px;height:1200px;overflow:hidden;background:var(--white)}
  .flyer{position:relative;width:853px;height:1200px;overflow:hidden;background:var(--white);font-family:"Open Sans",Arial,sans-serif;color:var(--ink)}
  .swoosh{position:absolute;left:0;top:0;width:853px;height:320px}
  .brand{position:absolute;left:42px;top:40px;display:flex;align-items:center;gap:14px}
  .brand-dot{width:44px;height:44px;border-radius:50%;background:var(--magenta)}
  .brand-name{font-family:"Open Sans",Arial,sans-serif;font-weight:600;font-size:60px;letter-spacing:-1px;color:var(--magenta)}
  .price-panel{position:absolute;left:0;top:540px;width:853px;height:610px;background:var(--blush)}
  .intro{position:absolute;left:42px;top:318px;width:390px}
  .title{font-family:"Libre Baskerville",Georgia,serif;font-style:italic;font-weight:700;font-size:27px;line-height:1.25;color:var(--magenta);text-transform:uppercase}
  .esl{margin-top:24px;font-family:"Libre Baskerville",Georgia,serif;font-style:italic;font-weight:700;font-size:19px;line-height:1.4;color:var(--magenta)}
  .intro p.body{margin-top:18px;font-size:17px;line-height:1.45}
  .services{position:absolute;left:470px;top:262px;width:350px;height:500px;background:var(--white);border-top:6px solid var(--magenta);box-shadow:0 6px 18px rgba(125,16,68,.18);padding:30px 34px}
  .services h2{font-family:"Open Sans",Arial,sans-serif;font-weight:600;font-size:21px;color:var(--magenta);margin-bottom:14px}
  .services ul{list-style:none}
  .services li{position:relative;padding-left:22px;font-size:18.5px;line-height:1.52;color:var(--ink)}
  .services li::before{content:"";position:absolute;left:2px;top:11px;width:9px;height:9px;border-radius:50%;background:var(--magenta)}
  .pricing{position:absolute;left:42px;top:690px;width:780px}
  .pricing h2{font-family:"Libre Baskerville",Georgia,serif;font-style:italic;font-weight:700;font-size:27px;color:var(--magenta);margin-bottom:10px}
  .pricing ul{list-style:none}
  .pricing li{position:relative;padding-left:16px;font-size:16.5px;line-height:1.42;margin-bottom:2px}
  .pricing li::before{content:"·";position:absolute;left:2px;top:0;font-weight:700}
  .pricing li.highlight{color:var(--magenta);font-style:italic;font-weight:600}
  .pricing em{font-style:italic}
  .graduate{position:absolute;left:28px;top:905px;width:320px;height:225px;border-radius:8px;background:linear-gradient(160deg,#3a3034 0%,#1c1719 55%,#e9ddd0 100%)}
  .testimonial{position:absolute;left:455px;top:930px;width:370px}
  .quote-mark{position:absolute;left:-62px;top:-12px;font-family:"Libre Baskerville",Georgia,serif;font-size:90px;line-height:1;color:var(--magenta)}
  .testimonial h3{font-family:"Libre Baskerville",Georgia,serif;font-style:italic;font-weight:700;font-size:17px;color:var(--magenta);margin-bottom:4px}
  .testimonial blockquote{font-family:"Libre Baskerville",Georgia,serif;font-style:italic;font-size:14.5px;line-height:1.45;color:var(--ink)}
  .testimonial cite{display:block;text-align:right;margin-top:10px;font-family:"Libre Baskerville",Georgia,serif;font-style:italic;font-size:14px;line-height:1.4}
  .footer{position:absolute;left:0;bottom:0;width:853px;height:50px;background:var(--magenta);color:var(--white);display:flex;align-items:center;padding-left:42px;font-family:"Libre Baskerville",Georgia,serif;font-style:italic;font-size:16.5px}
</style>
</head>
<body>
<div class="flyer">
  <svg class="swoosh" viewBox="0 0 853 320" aria-hidden="true">
    <path d="M300 0 H853 V230 C700 150 560 60 300 0 Z" fill="var(--magenta)"/>
    <path d="M520 0 H853 V150 C760 90 650 30 520 0 Z" fill="var(--magenta-dark)"/>
    <path d="M0 150 C250 120 520 170 853 260 V300 C560 230 300 190 0 205 Z" fill="var(--magenta-soft)" opacity=".85"/>
    <path d="M0 205 C300 190 560 230 853 300 V320 H0 Z" fill="var(--magenta)"/>
  </svg>

  <div class="brand">
    <span class="brand-dot"></span>
    <span class="brand-name">Lexmarka</span>
  </div>

  <div class="price-panel"></div>

  <section class="intro">
    <h1 class="title">Professional, English Language Proofreading</h1>
    <p class="esl">Help with English as a second language (ESL).</p>
    <p class="body">Proofreading by a native English speaker with an English Honours degree.</p>
    <p class="body">Includes correct all English language errors, spelling and grammar mistakes, reference checking and editing for style, coherence and clarity.</p>
  </section>

  <aside class="services">
    <h2>We will proofread your:</h2>
    <ul>
      <li>essays &amp; assignments</li>
      <li>theses</li>
      <li>resumes</li>
      <li>business correspondence</li>
      <li>training manuals</li>
      <li>newsletters</li>
      <li>advertising copy</li>
      <li>brochures, catalogues &amp; media releases</li>
      <li>websites</li>
      <li>presentations &amp; speeches</li>
      <li>novels &amp; short stories</li>
    </ul>
  </aside>

  <section class="pricing">
    <h2>PRICE GUIDE:</h2>
    <ul>
      <li>Prices start at only $20 (short menus, flyers, letters).</li>
      <li>Discounts for not-for-profit organisations and students.</li>
      <li class="highlight">Great student discount rate: $25 per hour (roughly 1000 words - 4 pages - of well-written text).</li>
      <li>Package deals on documents over 50,000 words.</li>
      <li>Fast, negotiable time-frames <em>(same day service available by special arrangement).</em></li>
    </ul>
  </section>

  <div class="graduate" role="img" aria-label="Photo of a graduation cap resting on a rolled diploma"></div>

  <section class="testimonial">
    <span class="quote-mark">“</span>
    <h3>Testimonial:</h3>
    <blockquote>Sarah understood our requirements quickly and has been fantastic at delivering quality work, on time and within agreed budget. It's a pleasure to work with her.</blockquote>
    <cite>- Rachel Moreton<br>Operations Manager, Calverly Group</cite>
  </section>

  <footer class="footer">Contact us for an obligation free quote: 0400 123 456 / hello@lexmarka.com.au</footer>
</div>
</body>
</html>
```